Quirky Label Design for an Exciting UK-Based Organic Skincare Company!

We need label designs across our range of products, we are a high quality yet quirky organic skincare company called Gently Lumora, we use frosted glass packaging, and we are just wanting one design done for now, but the winning designer we would want to work with to design the rest of the labels for us. We also want them to design business cards and other literature at some point and maybe even a website page.

Our label design will go on a 63mm tall frosted glass jar which is 62mm in diameter. The actual label dimensions should be, 170 mm (W) x 50 mm (H). The idea is so that it wraps around the whole jar with the design at one side (at the front) and the ingredients on another (at the back).

LABEL 1
Organic Polynesian Whipped Body Butter
Vanilla Bean
120ml

Made with Organic Shea and Cocoa Butters and exotic Monoi de Tahiti

Ingredients (INCI): Organic Raw Shea Butter (Butyrospermum Parkii), Organic Raw Cocoa Butter (Theobroma Cacao), Monoi de Tahiti (Coconut (Cocos nucifera) oil (and) Tiare (Gardenia tahitensis) flower), Organic Sweet Almond Oil (Prunus Amygdalus Dulcis), Organic Madagascan Vanilla Extract (Vanillin)

Handmade by Gently Lumora Ltd
14 Quillfield Lane, Bournemouth BH2 9RT, UK
Batch:

OPTIONAL WRITING (if it fits in):
100% Natural and Organic
Intensely Moisturising

LABEL 2
Mango Smoothie
120ml

Ingredients (INCI): Organic Raw Shea Butter (Butyrospermum Parkii), Organic Raw Cocoa Butter (Theobroma Cacao), Monoi de Tahiti (Coconut (Cocos nucifera) oil (and) Tiare (Gardenia tahitensis) flower), Organic Sweet Almond Oil (Prunus Amygdalus Dulcis), Organic Mango Flavour (Aroma)

Batch:

100% Natural and Organic
Intensely Moisturising

I have attached a picture of the jar we use and the lid we use for these products, as well as our logo. I've also attached a 'Handmade in Dorset' stamp which we'd like to go on there if possible, along with a shelf life symbol.

I am thinking the background colour of the labels will be either white or even brown paper colour. Perhaps it would be interesting to see it in both. UPDATE: We have decided on white background now, not brown.

The final design should denote handmade, organic, high quality, pure, yet quirky and original / unique. I am thinking perhaps a seemingly hand-drawn black leaf outline? Could fit the bill, but as I say, up to you. Something that says handmade yet professional.

I'd like to have the original Photoshop files from the winning designer so we can use them as a template for the rest of our horizontal labels.

Target Market(s)

Everyone that appreciates a good quality skincare product focusing on natural & organic. Price is mid-range to high

Industry/Entity Type

It Company

Requirements
Must have
• Must make the product look high quality & organic yet quirky and accessible. Must have our logo and the shelf life symbol and the writing as above.
Nice to have
• Nice to have the 'handmade' stamp attached, but not absolutely necessary if it doesn't fit within your design.

```html
<!DOCTYPE html>
<html lang="en">
<head>
<meta charset="utf-8">
<title>Gently Lumora – Vanilla Bean Whipped Body Butter Label</title>
<link href="https://fonts.googleapis.com/css2?family=Kalam:wght@400;700&family=Open+Sans:wght@400&display=swap" rel="stylesheet">
<style>
  :root {
    --page-bg: #eef0ef;
    --label-white: #ffffff;
    --label-grey: #d9dcdb;
    --glow-yellow: #f6e27a;
    --brand-brown: #5e3b1c;
    --text-dark: #2b2b2b;
    --leaf-green: #b9cf72;
    --leaf-pale: #dfe6a6;
    --cream: #f3efb0;
    --bean-brown: #4a2c18;
  }
  * { margin: 0; padding: 0; box-sizing: border-box; }
  html, body {
    width: 1200px;
    height: 1172px;
    overflow: hidden;
    background: var(--page-bg);
  }
  .canvas {
    position: relative;
    width: 1200px;
    height: 1172px;
  }
  .label {
    position: absolute;
    left: 67px;
    top: 278px;
    width: 1065px;
    height: 615px;
    overflow: hidden;
    background:
      radial-gradient(ellipse 300px 260px at 760px 230px, rgba(246,226,122,0.85), rgba(246,226,122,0) 70%),
      radial-gradient(ellipse 240px 180px at 60px 560px, rgba(246,226,122,0.5), rgba(246,226,122,0) 70%),
      linear-gradient(90deg, var(--label-grey) 0%, var(--label-white) 18%, var(--label-white) 80%, var(--label-grey) 100%);
  }
  .art {
    position: absolute;
  }
  .art--bamboo-leaves {
    left: 660px;
    top: 0;
    width: 405px;
    height: 400px;
    background: radial-gradient(ellipse at 65% 40%, rgba(185,207,114,0.75), rgba(223,230,166,0.35) 60%, rgba(223,230,166,0) 80%);
  }
  .art--cream-and-vanilla {
    left: 615px;
    top: 320px;
    width: 405px;
    height: 290px;
    background: radial-gradient(ellipse at 45% 45%, var(--cream) 0%, rgba(243,239,176,0.7) 45%, rgba(74,44,24,0.25) 75%, rgba(74,44,24,0) 90%);
  }
  .art--corner-leaves {
    left: 0;
    top: 400px;
    width: 240px;
    height: 210px;
    background: radial-gradient(ellipse at 40% 60%, rgba(185,207,114,0.8), rgba(223,230,166,0.3) 65%, rgba(223,230,166,0) 85%);
  }
  .brand-name {
    position: absolute;
    left: 100px;
    top: 60px;
    width: 550px;
    text-align: center;
    font-family: "Kalam", cursive;
    font-weight: 700;
    font-size: 118px;
    line-height: 0.95;
    color: var(--brand-brown);
    text-transform: uppercase;
  }
  .product-type {
    position: absolute;
    left: 150px;
    top: 385px;
    width: 450px;
    text-align: center;
    font-family: "Open Sans", sans-serif;
    font-size: 30px;
    line-height: 38px;
    color: var(--text-dark);
  }
  .scent {
    position: absolute;
    left: 190px;
    top: 520px;
    width: 370px;
    text-align: center;
    font-family: "Kalam", cursive;
    font-weight: 400;
    font-size: 46px;
    line-height: 1;
    color: var(--brand-brown);
    letter-spacing: 2px;
  }
  .volume {
    position: absolute;
    right: 32px;
    top: 568px;
    font-family: "Open Sans", sans-serif;
    font-size: 24px;
    color: var(--text-dark);
  }
</style>
</head>
<body>
  <main class="canvas">
    <section class="label">
      <div class="art art--bamboo-leaves" role="img" aria-label="Illustration of pale green bamboo leaves"></div>
      <div class="art art--corner-leaves" role="img" aria-label="Illustration of green leaves in the lower corner"></div>
      <div class="art art--cream-and-vanilla" role="img" aria-label="Illustration of a bowl of whipped body butter with a vanilla flower and vanilla pods"></div>

      <h1 class="brand-name">Gently<br>Lumora</h1>
      <p class="product-type">Organic Polynesian<br>Whipped Body Butter</p>
      <p class="scent">Vanilla Bean</p>
      <p class="volume">120ml</p>
    </section>
  </main>
</body>
</html>
```